New Alcoholic Spiked Seltzer Line

We need a can design for a line of low calorie alcoholic seltzer. This product is a sparkling water and vodka drink with no sugar added in a slim 12 oz can.

This is a lighter, healthier, alternative to the sugary ready-to-drinks on the market. The product contains only 3 ingredients: Vodka, Water and Natural Flavors. It has only 100 calories but still has 5% alcohol, so you don't need to sacrifice alcohol to cut calories.

This product also does not contain any preservatives.

We want this design to communicate the following objectives to the consumer and in this order:

1. Appetizing product
2.Low calorie
3.Communicate the type of beverage (Spiked Seltzer)

The brand name of the product is ZIVA.

The flavor of the product needed to be used for the design is Mango-Orange.

Comparable products are:

www.brightfizzcanhouse.example/
https://www.lumabubble.example
https://palefernco.example/

The designs should not infringe or copy the creative directions of the products mentionned above. They are only given so that you can better understand the type of product we are developing.

Target Market(s)

Young Professional women between the ages of 25 and 44

Industry/Entity Type

Product

Colors

Designer to choose colors to be used in the design.

Requirements
Must have
• Design extendibility, meaning it can be adapted for other flavors.
• This is a new category in the market we are targeting, so consumers must easily be able to identify what type of product this is.

```html
<!DOCTYPE html>
<html lang="en">
<head>
<meta charset="utf-8">
<title>ZIVA Spiked Seltzer – Mango-Orange Can Label</title>
<link rel="stylesheet" href="https://fonts.googleapis.com/css2?family=Josefin+Sans:wght@300&family=Montserrat:wght@700&family=Yellowtail&family=Tinos:wght@400;700&family=Kalam:wght@400&display=block">
<style>
  :root {
    --page-bg: #eceef1;
    --label-white: #ffffff;
    --ink-dark: #1d1d1d;
    --brand-green: #2f8a6e;
    --band-green: #2e8b6f;
    --citrus: #e06a12;
    --citrus-deep: #c8500c;
    --citrus-light: #f6a441;
    --mango-yellow: #f7c642;
    --rule-orange: #e4731c;
  }
  * { margin: 0; padding: 0; box-sizing: border-box; }
  html, body {
    width: 1200px;
    height: 2612px;
    overflow: hidden;
    background: var(--page-bg);
  }
  .can-label {
    position: absolute;
    left: 100px;
    top: 300px;
    width: 1000px;
    height: 1560px;
    background: var(--label-white);
    overflow: hidden;
  }
  .rule {
    position: absolute;
    left: 0;
    width: 100%;
    height: 14px;
    background: var(--rule-orange);
  }
  .rule--top { top: 40px; }
  .rule--bottom { bottom: 40px; }

  .brand-lockup {
    position: absolute;
    left: 160px;
    top: 180px;
    width: 700px;
    height: 270px;
  }
  .brand-name {
    position: absolute;
    left: 0;
    top: 0;
    font-family: "Josefin Sans", sans-serif;
    font-weight: 300;
    font-size: 200px;
    line-height: 1;
    letter-spacing: 6px;
    color: var(--ink-dark);
  }
  .category-tag {
    position: absolute;
    left: 240px;
    top: 172px;
    padding: 4px 28px;
    background: var(--label-white);
    border-radius: 26px;
    box-shadow: 0 6px 18px rgba(0,0,0,0.18);
    font-family: "Kalam", cursive;
    font-size: 62px;
    line-height: 1.2;
    color: var(--brand-green);
    white-space: nowrap;
  }
  .claim-band {
    position: absolute;
    left: 164px;
    top: 470px;
    width: 656px;
    height: 56px;
    background: var(--band-green);
    color: #fff;
    font-family: "Montserrat", sans-serif;
    font-weight: 700;
    font-size: 34px;
    line-height: 56px;
    text-align: center;
    letter-spacing: 1px;
    white-space: nowrap;
  }
  .abv {
    position: absolute;
    right: 180px;
    top: 548px;
    font-family: "Tinos", serif;
    font-size: 38px;
    color: var(--ink-dark);
  }
  .flavor-name {
    position: absolute;
    left: 0;
    width: 100%;
    top: 610px;
    z-index: 2;
    text-align: center;
    font-family: "Yellowtail", cursive;
    font-weight: 400;
    font-size: 120px;
    line-height: 1.2;
    color: var(--citrus);
    white-space: nowrap;
  }
  .flavor-band {
    position: absolute;
    left: 0;
    top: 940px;
    width: 100%;
    height: 220px;
    background: linear-gradient(180deg, var(--citrus-deep), var(--citrus) 50%, var(--citrus-deep));
  }
  .fruit-art {
    position: absolute;
    left: 250px;
    top: 800px;
    width: 500px;
    height: 500px;
    border-radius: 50%;
    background: radial-gradient(circle at 45% 40%, var(--mango-yellow), var(--citrus-light) 45%, var(--citrus) 100%);
  }
  .calorie-claim {
    position: absolute;
    left: 0;
    width: 100%;
    top: 1370px;
    text-align: center;
    font-family: "Tinos", serif;
    font-weight: 700;
    font-size: 48px;
    letter-spacing: 2px;
    color: var(--ink-dark);
  }
</style>
</head>
<body>
  <main class="can-label">
    <div class="rule rule--top"></div>

    <div class="brand-lockup">
      <div class="brand-name">ZIVA</div>
      <div class="category-tag">Spiked Seltzer</div>
    </div>

    <div class="claim-band">MADE WITH NATURAL FLAVORS</div>
    <div class="abv">5% alc./vol.</div>

    <h1 class="flavor-name">Mango-Orange</h1>

    <div class="flavor-band"></div>
    <div class="fruit-art" role="img" aria-label="Splashing juice with sliced oranges and a cut mango"></div>

    <p class="calorie-claim">ONLY 100 CALORIES</p>

    <div class="rule rule--bottom"></div>
  </main>
</body>
</html>
```